Place holder for book called SALT LANTERN WINTERS

I'm relying on your imaginative genius because I have no suggestions for you. Attached is a picture of the author when young if it will be of help. The only other info I can offer is that the author uses the alphabet as a theme.

Book info:
Title: SALT LANTERN WINTERS
Author: MARGOT KWELLAND

This is a memoir. It's a story of daring to hope when things seem hopeless, of problems when changing countries, of making success of dross. I'm looking for a design that is daring, eye-catching but promises hope. I hope it's not impossible.

Can you give me a place holder for the book to go onto my website and for pre-publicity? Then, in 6-9 months I'll pay another $150 for the completion of hardcover, paperback and ebook covers.

```html
<!DOCTYPE html>
<html lang="en">
<head>
<meta charset="utf-8">
<title>Salt Lantern Winters — Margot Kwelland</title>
<link rel="stylesheet" href="https://fonts.googleapis.com/css2?family=Bebas+Neue&display=swap">
<style>
  :root {
    --sky-top: #3f4b57;
    --sky-mid: #6f7573;
    --sky-warm: #a8967a;
    --sky-glow: #c4ae8a;
    --treeline: #1c2630;
    --ground: #3a3630;
    --ink: #ffffff;
  }
  html, body {
    margin: 0;
    padding: 0;
    width: 935px;
    height: 1200px;
    overflow: hidden;
    background: #c8c8c8;
  }
  .book-cover {
    position: relative;
    width: 935px;
    height: 1200px;
    overflow: hidden;
  }
  .cover-photo,
  .cover-type {
    position: absolute;
    inset: 0;
    width: 935px;
    height: 1200px;
    display: block;
  }
  .title-word,
  .author-name {
    font-family: "Bebas Neue", "Oswald", sans-serif;
    fill: var(--ink);
  }
  .title-rule { fill: var(--ink); }
</style>
</head>
<body>
<main class="book-cover">
  <svg class="cover-photo" viewBox="0 0 935 1200" role="img" aria-label="Photograph of a cloudy dusk sky over a dark treeline and open field">
    <defs>
      <linearGradient id="sky" x1="0" y1="0" x2="0.35" y2="1">
        <stop offset="0" stop-color="var(--sky-top)"/>
        <stop offset="0.35" stop-color="var(--sky-mid)"/>
        <stop offset="0.7" stop-color="var(--sky-warm)"/>
        <stop offset="0.88" stop-color="var(--sky-glow)"/>
        <stop offset="1" stop-color="var(--sky-warm)"/>
      </linearGradient>
      <linearGradient id="land" x1="0" y1="0" x2="0" y2="1">
        <stop offset="0" stop-color="var(--treeline)"/>
        <stop offset="0.7" stop-color="var(--treeline)"/>
        <stop offset="1" stop-color="var(--ground)"/>
      </linearGradient>
      <radialGradient id="glow" cx="0.75" cy="0.55" r="0.6">
        <stop offset="0" stop-color="#d8c4a0" stop-opacity="0.45"/>
        <stop offset="1" stop-color="#d8c4a0" stop-opacity="0"/>
      </radialGradient>
    </defs>
    <rect width="935" height="1200" fill="url(#sky)"/>
    <rect width="935" height="1200" fill="url(#glow)"/>
    <rect y="1060" width="935" height="140" fill="url(#land)"/>
  </svg>

  <svg class="cover-type" viewBox="0 0 935 1200" aria-labelledby="cover-title">
    <title id="cover-title">Salt Lantern Winters by Margot Kwelland</title>
    <g class="title-block">
      <rect class="title-rule" x="124" y="194" width="220" height="30"/>
      <rect class="title-rule" x="590" y="194" width="232" height="30"/>
      <text class="title-word" x="467" y="262" font-size="126" text-anchor="middle">SALT</text>
      <text class="title-word" x="124" y="460" font-size="210" textLength="698" lengthAdjust="spacingAndGlyphs">LANTERN</text>
      <text class="title-word" x="124" y="830" font-size="370" textLength="698" lengthAdjust="spacingAndGlyphs">WINTERS</text>
    </g>
    <text class="author-name" x="467" y="1108" font-size="56" letter-spacing="5" text-anchor="middle">MARGOT KWELLAND</text>
  </svg>
</main>
</body>
</html>
```